New Business Card Design Project

I need a design for business cards, i am an electrical business called "Vantor Electrical and Communications" i need the cards to be double sided with the company logo on the back (attached) the front needs to say my company name, web site, email address, telephone number, and ABN number and electrical license number. I am open to different arrangements of the information but would like the background to be incorporating something electrical or something that looks smart. open to all additional ideas also.

The company colours are orange and grey see logo attached.

Business Name: Vantor Electrical and Communications
Website: vantorelectricalandcomms.example.au
Email: dean@vantorelectricalandcomms.example.au
Telephone(mobile): 0481290736
ABN: 71829304516
Lic No: 483027D

Target Market(s)

Business entities, Project Managers, Accounts, Clients

Industry/Entity Type

Electrician

Contact Information for Business Card

I need a design for business cards, i am an electrical business called "Vantor Electrical and Communications" i need the cards to be double sided with the company logo on the back (attached) the front needs to say my company name

Font styles to use
Serif
Sans Serif

Colors
f37122
5c5c5c

Requirements
Must have
• Must have the Logo on the back open to different ways of it being on the back but had in mind to keep it central but again open to other options
Nice to have
• A real modern cool background that is eye catching yet contemporary
Should not have
• No backgrounds of a light bulb or plug or anything like that

```html
<!DOCTYPE html>
<html lang="en">
<head>
<meta charset="utf-8">
<title>Vantor Electrical and Communications – Business Card</title>
<link rel="stylesheet" href="https://fonts.googleapis.com/css2?family=Open+Sans:wght@400;600;700&display=swap">
<style>
  :root {
    --stage: #3b3634;
    --card-black: #050505;
    --card-glow: #2e2e2e;
    --accent: #f37122;
    --accent-light: #f79450;
    --brand-grey: #5c5c5c;
    --grey-light: #a9a9a9;
    --text-light: #f2f2f2;
  }
  * { box-sizing: border-box; margin: 0; padding: 0; }
  html, body {
    width: 1200px; height: 844px; overflow: hidden;
    background: var(--stage);
    font-family: "Open Sans", Arial, sans-serif;
  }
  .stage {
    position: relative; width: 1200px; height: 844px;
    display: flex; align-items: center; justify-content: center; gap: 40px;
  }
  .card {
    position: relative; width: 520px; height: 300px;
    background: var(--card-black); overflow: hidden;
  }
  /* Front */
  .card--front {
    background: linear-gradient(160deg, #1e1e1e 0%, var(--card-black) 55%);
  }
  .band {
    position: absolute; left: 0; right: 0; height: 11px;
    background: linear-gradient(var(--accent-light), var(--accent));
  }
  .band--top { top: 12px; }
  .band--bottom { bottom: 12px; }
  .contact {
    position: absolute; top: 23px; bottom: 23px; left: 20px; right: 20px;
    text-align: center;
    display: flex; flex-direction: column; justify-content: center;
    color: var(--text-light);
  }
  .contact__name { color: var(--accent); font-weight: 700; font-size: 18px; line-height: 1.25; }
  .contact__role { font-size: 12px; line-height: 1.4; color: var(--text-light); }
  .contact__company {
    font-size: 11px; line-height: 1.4; color: var(--grey-light);
    letter-spacing: 1.5px; text-transform: uppercase; font-weight: 600;
  }
  .contact__line { font-size: 14px; line-height: 1.45; }
  .contact__line--strong { font-size: 15px; font-weight: 700; }
  .contact__label { color: var(--accent); font-weight: 700; }
  .contact__group { margin-bottom: 18px; }
  .contact__group:last-child { margin-bottom: 0; }
  /* Back */
  .card--back {
    background: radial-gradient(ellipse at 55% 50%, var(--card-glow) 0%, var(--card-black) 65%);
  }
  .brand {
    position: absolute; inset: 0;
    display: flex; align-items: center; justify-content: center;
    color: var(--text-light); font-weight: 600; font-size: 22px; letter-spacing: 0.5px;
  }
  .tab {
    position: absolute; width: 22px; height: 36px;
    background: linear-gradient(var(--accent-light), var(--accent));
  }
  .tab::after {
    content: ""; position: absolute; top: 0; bottom: 0; width: 4px; background: var(--brand-grey);
  }
  .tab--left { left: 0; top: 196px; }
  .tab--left::after { left: 0; }
  .tab--right { right: 0; top: 64px; }
  .tab--right::after { right: 0; }
</style>
</head>
<body>
  <main class="stage">
    <section class="card card--front" aria-label="Business card front">
      <div class="band band--top"></div>
      <div class="contact">
        <div class="contact__group">
          <p class="contact__name">Dean Harlow</p>
          <p class="contact__role">Director</p>
          <p class="contact__company">Vantor Electrical &amp; Communications</p>
        </div>
        <div class="contact__group">
          <p class="contact__line contact__line--strong"><span class="contact__label">ABN:</span> 71829304516</p>
          <p class="contact__line contact__line--strong"><span class="contact__label">Lic No:</span> 483027D</p>
        </div>
        <div class="contact__group">
          <p class="contact__line"><span class="contact__label">Phone:</span> 0481290736</p>
          <p class="contact__line"><span class="contact__label">Email:</span> dean@vantorelectricalandcomms.example.au</p>
          <p class="contact__line"><span class="contact__label">Website:</span> vantorelectricalandcomms.example.au</p>
        </div>
      </div>
      <div class="band band--bottom"></div>
    </section>

    <section class="card card--back" aria-label="Business card back">
      <div class="tab tab--right"></div>
      <div class="tab tab--left"></div>
      <p class="brand">Vantor Electrical &amp; Communications</p>
    </section>
  </main>
</body>
</html>
```